Marketing One-Sheet for Security Deposit Claim Notice

I need a one-sheet flyer formatted for email distribution — optimized as a JPEG/PNG that I can insert into Constant Contact or Outlook. I do not want to attach it to an email, but insert it in the email we send out. I would like it to look professional but engaging. Some images would be good, but want to make sure it reads well if images do not load for the recipients. The text is in the attached Word document, but I am open to changes/ideas that may be better for marketing purposes. I included the URLs for some of the links I would like in the one-sheet that is clickable. The logo for the business is being uploaded on the Word document. Proposed text is also uploaded in a Word document. Thank you.

Target Market(s)

Landlords, Real Estate Agents, Property Managers

Industry/Entity Type

Legal

Requirements
Must have
• Professional but appealing design. The One-sheet is going to be placed in the body of emails, not as an attachment.
Nice to have
• Include our logo for the business and the web links please.
Should not have
• Images can be ok, but it needs to look right if images do not download from the email sent out.

```html
<!DOCTYPE html>
<html lang="en">
<head>
<meta charset="utf-8">
<title>Security Deposit Claim Notice</title>
<link href="https://fonts.googleapis.com/css2?family=Poppins:ital,wght@0,400;0,500;0,600;0,700;0,800;1,400&family=Cinzel:wght@600&display=swap" rel="stylesheet">
<style>
  :root {
    --red: #ee1f26;
    --red-deep: #c1232a;
    --maroon: #7a1013;
    --pink: #f8b4a6;
    --ink: #1c1c1c;
    --white: #ffffff;
    --link: #2f56a5;
  }
  * { box-sizing: border-box; margin: 0; padding: 0; }
  html, body { width: 848px; height: 1200px; overflow: hidden; background: var(--white); }
  body { font-family: "Poppins", sans-serif; color: var(--ink); position: relative; }

  .brand { position: absolute; top: 18px; left: 0; width: 848px; text-align: center; }
  .brand-name { display: inline-flex; align-items: center; gap: 10px; font-family: "Cinzel", serif; font-weight: 600; font-size: 30px; color: var(--red-deep); letter-spacing: 1px; }
  .brand-mark { width: 22px; height: 22px; background: var(--red-deep); }
  .brand-contact { font-size: 12px; font-weight: 600; color: var(--red-deep); line-height: 1.35; margin-top: 4px; }
  .brand-contact .phone { color: var(--ink); font-size: 13px; }

  .headline { position: absolute; top: 220px; width: 848px; text-align: center; }
  .headline h1 { font-size: 24px; font-weight: 800; color: var(--red); letter-spacing: 0.3px; }
  .headline p { font-size: 15px; margin-top: 4px; }

  .uses { position: absolute; top: 330px; left: 50px; display: flex; gap: 0; }
  .use { display: flex; align-items: center; gap: 12px; font-size: 13px; line-height: 1.25; }
  .use:nth-child(1) { width: 220px; }
  .use:nth-child(2) { width: 266px; }
  .use:nth-child(3) { width: 260px; }
  .use-num { width: 37px; height: 37px; flex: none; background: var(--red-deep); color: var(--white); font-weight: 700; font-size: 17px; display: flex; align-items: center; justify-content: center; }

  .band { position: absolute; left: 0; width: 848px; display: flex; }
  .offer { top: 422px; height: 85px; }
  .offer .lead { width: 449px; background: var(--red); color: var(--white); font-size: 22px; line-height: 1.1; padding: 12px 0 0 52px; }
  .offer .price { flex: 1; background: var(--red-deep); color: var(--white); font-weight: 800; font-size: 29px; display: flex; align-items: center; padding-left: 88px; gap: 30px; margin-right: 4px; }

  .warning { top: 507px; height: 116px; background: var(--maroon); color: var(--white); flex-direction: column; align-items: center; justify-content: center; font-size: 21px; line-height: 1.3; text-align: center; padding-bottom: 8px; }

  .consequences { top: 623px; height: 75px; background: var(--red); color: var(--white); flex-direction: column; align-items: center; justify-content: center; font-size: 13px; font-weight: 500; line-height: 1.35; text-align: center; }

  .note { position: absolute; top: 710px; left: 56px; width: 740px; font-size: 12.5px; line-height: 1.5; text-align: center; }

  .commercial { top: 782px; height: 109px; }
  .commercial .lead { width: 449px; background: var(--pink); color: var(--white); font-size: 25px; line-height: 1.2; padding: 18px 0 0 52px; }
  .commercial .price { flex: 1; background: var(--red); color: var(--white); font-weight: 800; font-size: 54px; display: flex; align-items: center; padding-left: 170px; }

  .contact { position: absolute; top: 958px; width: 848px; text-align: center; }
  .contact h2 { font-size: 27px; font-weight: 700; color: var(--red); }
  .contact .pitch { font-size: 14px; font-style: italic; margin-top: 14px; }
  .contact .details { font-size: 14px; line-height: 1.4; margin-top: 18px; }
  .contact .details strong { font-weight: 700; }
  .contact .links { font-size: 14px; line-height: 1.45; margin-top: 22px; }
  .contact .links a { color: var(--link); text-decoration: underline; }
</style>
</head>
<body>
  <header class="brand">
    <div class="brand-name"><span class="brand-mark"></span>Keystone Tenancy Law</div>
    <div class="brand-contact">KeystoneTenancyLaw.com<br><span class="phone">1(800) 555-0142</span></div>
  </header>

  <section class="headline">
    <h1>SECURITY DEPOSIT CLAIM NOTICE</h1>
    <p>Keep the tenant’s Security Deposit</p>
  </section>

  <ol class="uses">
    <li class="use"><span class="use-num">1</span>Cover unpaid Rent</li>
    <li class="use"><span class="use-num">2</span>Apply to legal fees and costs</li>
    <li class="use"><span class="use-num">3</span>Charge against Damages to the Property</li>
  </ol>

  <section class="band offer">
    <div class="lead">we prepare security deposit claim notices</div>
    <div class="price"><span>FLAT FEE</span><span>$350</span></div>
  </section>

  <section class="band warning">
    <p>Follow Florida law to keep the Deposit</p>
    <p>If the Security Deposit Claim is not made correctly and on time, then:</p>
  </section>

  <section class="band consequences">
    <p>Tenant is automatically entitled to their full deposit back</p>
    <p>No claim against the deposit can be made</p>
    <p>Tenant can sue and recover the deposit and thousands in legal fees</p>
  </section>

  <p class="note">There are lawyers that specialize in representing tenants and go after landlords that do not make a proper claim against the security deposit. They sue and win their cases and get thousands of dollars in legal fees against Landlords, even if the tenant owes unpaid rent.</p>

  <section class="band commercial">
    <div class="lead">For commercial properties, the flat legal fee is</div>
    <div class="price">$450.</div>
  </section>

  <section class="contact">
    <h2>Contact Us</h2>
    <p class="pitch">Hire Us to prepare and serve to the tenant the security deposit claim</p>
    <p class="details">Keystone Tenancy Law<br>KeystoneTenancyLaw.com<br><strong>1800-555-0142</strong></p>
    <p class="links">[more information – <a href="https://keystonetenancylaw.com/keeping-security-deposits/">https://keystonetenancylaw.com/keeping-security-deposits/</a><br>[request our hiring documents <a href="https://keystonetenancylaw.com/hire-lawyer/">- https://keystonetenancylaw.com/hire-lawyer/</a></p>
  </section>
</body>
</html>
```